Lantern Hill Publicity is a new boutique Press Office with a small roster of well-chosen clients across an array of disciplines; from Art and Technology to Restaurants and Fashion. Based in Greenpoint Brooklyn, Lantern Hill Publicity achieves outstanding results through hard work, tenacity, efficiency and a sense of humor. We need a simple, versatile and classic design. We would like each side of the card to be white text on a black background.

Boutique

```html
<!DOCTYPE html>
<html lang="en">
<head>
<meta charset="utf-8">
<title>Lantern Hill Publicity — Business Cards</title>
<link href="https://fonts.googleapis.com/css2?family=Libre+Baskerville:wght@400;700&display=swap" rel="stylesheet">
<style>
  :root {
    --backdrop: #3f3f40;
    --card: #232223;
    --ink: #ffffff;
    --ink-soft: #e6e6e6;
  }
  html, body {
    margin: 0;
    padding: 0;
    width: 1200px;
    height: 810px;
    overflow: hidden;
    background: var(--backdrop);
  }
  .canvas {
    width: 1200px;
    height: 810px;
    display: flex;
    flex-direction: column;
    align-items: center;
    justify-content: center;
    gap: 40px;
    font-family: "Libre Baskerville", "Times New Roman", serif;
    color: var(--ink);
  }
  .card {
    width: 620px;
    height: 354px;
    background: var(--card);
    border-radius: 18px;
    box-sizing: border-box;
    display: flex;
    flex-direction: column;
    align-items: center;
    justify-content: center;
    text-align: center;
  }
  .brand-name {
    margin: 0;
    font-size: 24px;
    font-weight: 400;
    letter-spacing: 0.16em;
    text-transform: uppercase;
    color: var(--ink);
  }
  .card--front .brand-name {
    font-size: 28px;
  }
  .website {
    margin: 48px 0 0;
    font-size: 13px;
    letter-spacing: 0.2em;
    color: var(--ink-soft);
  }
  .person {
    margin-top: 34px;
  }
  .person-name {
    margin: 0;
    font-size: 19px;
    font-weight: 700;
  }
  .person-role {
    margin: 6px 0 0;
    font-size: 13px;
    color: var(--ink-soft);
  }
  .contact {
    margin: 18px 0 0;
    font-size: 13px;
    line-height: 1.7;
    color: var(--ink-soft);
  }
  .contact p { margin: 0; }
</style>
</head>
<body>
  <main class="canvas">
    <section class="card card--front" aria-label="Card front">
      <h1 class="brand-name">Lantern Hill Publicity</h1>
      <p class="website">www.lanternhillpr.com</p>
    </section>

    <section class="card card--back" aria-label="Card back">
      <h2 class="brand-name">Lantern Hill Publicity</h2>
      <div class="person">
        <p class="person-name">Daniel Whitcombe</p>
        <p class="person-role">Owner &amp; Founder</p>
      </div>
      <div class="contact">
        <p>Cell: 917-555-0142 | E-mail: daniel@lanternhillpr.com</p>
        <p>Visit us: www.lanternhillpr.com</p>
      </div>
    </section>
  </main>
</body>
</html>
```